Revamp Landing Page

Our current landing page is http://lanternpubkq.com/ and we're looking for our site to look like this http://www.amberroomvk.com/. Classy, Sleek, Simple elegant.

The site should be desktop and mobile optimized.
Pages should be built out and the same structure. Drink Menu, Gallery, Events, Table Reservations, Membership, Press, Contact Us.

Feel free to use the images on our website.

```html
<!DOCTYPE html>
<html lang="en">
<head>
<meta charset="utf-8">
<title>Lantern Pub</title>
<link href="https://fonts.googleapis.com/css2?family=Open+Sans:wght@300;400;600&display=swap" rel="stylesheet">
<style>
  :root {
    --page-bg: #1a1a1a;
    --page-bg-deep: #101010;
    --page-bg-edge: #070707;
    --text: #f2f2f2;
    --text-soft: #d4d4d4;
    --frame: #e4e4e4;
    --photo-top: #d9b778;
    --photo-upper: #b9834c;
    --photo-mid: #7d4a2c;
    --photo-low: #4a2a1c;
    --photo-bottom: #2e1a12;
  }
  * { margin: 0; padding: 0; box-sizing: border-box; }
  html, body {
    width: 1200px;
    height: 1200px;
    overflow: hidden;
  }
  body {
    position: relative;
    font-family: "Open Sans", sans-serif;
    color: var(--text);
    background:
      radial-gradient(ellipse 70% 55% at 50% 48%, var(--page-bg) 0%, var(--page-bg-deep) 70%, var(--page-bg-edge) 100%);
  }
  .site-header {
    position: absolute;
    top: 272px;
    left: 0;
    width: 1200px;
    text-align: center;
  }
  .brand {
    font-size: 34px;
    font-weight: 300;
    letter-spacing: 2px;
    line-height: 46px;
    text-transform: uppercase;
    color: var(--text);
  }
  .main-nav {
    margin-top: 22px;
    display: flex;
    justify-content: center;
    gap: 21px;
    font-size: 12.5px;
    font-weight: 400;
  }
  .main-nav a {
    color: var(--text);
    text-decoration: none;
  }
  .hero {
    position: absolute;
    top: 396px;
    left: 159px;
    width: 882px;
    height: 434px;
    padding: 9px;
    background: var(--frame);
  }
  .hero-photo {
    position: relative;
    width: 100%;
    height: 100%;
    background: linear-gradient(180deg,
      var(--photo-top) 0%,
      var(--photo-upper) 30%,
      var(--photo-mid) 55%,
      var(--photo-low) 78%,
      var(--photo-bottom) 100%);
  }
  .hero-caption {
    position: absolute;
    left: 46px;
    right: 46px;
    bottom: 28px;
  }
  .hero-title {
    font-size: 15px;
    font-weight: 400;
    text-transform: uppercase;
    letter-spacing: 0.2px;
    color: var(--text);
  }
  .hero-text {
    margin-top: 6px;
    font-size: 9.5px;
    line-height: 1.25;
    color: var(--text);
  }
  .site-footer {
    position: absolute;
    top: 880px;
    left: 160px;
    width: 880px;
    height: 30px;
    display: flex;
    align-items: center;
  }
  .social {
    display: flex;
    gap: 6px;
    width: 180px;
  }
  .contact-line {
    flex: 1;
    text-align: center;
    font-size: 10px;
    text-transform: uppercase;
    color: var(--text-soft);
    white-space: nowrap;
  }
  .group-mark {
    width: 180px;
    text-align: right;
    font-size: 16px;
    font-weight: 400;
    color: var(--text);
  }
</style>
</head>
<body>
  <header class="site-header">
    <div class="brand">Lantern Pub</div>
    <nav class="main-nav">
      <a href="#">Drink Menu</a>
      <a href="#">Gallery</a>
      <a href="#">Events</a>
      <a href="#">Table Reservations</a>
      <a href="#">Membership</a>
      <a href="#">Press</a>
      <a href="#">Contact Us.</a>
    </nav>
  </header>

  <section class="hero">
    <div class="hero-photo" role="img" aria-label="Photo of the warmly lit bar with backlit bottle shelves, a long counter and stools">
      <div class="hero-caption">
        <h1 class="hero-title">Lantern Pub: A home away from home for the local community.</h1>
        <p class="hero-text">At Lantern Pub, it is our goal to make sure that you enjoy every moment in your experience.<br>Consider us your liaisons to happiness...</p>
      </div>
    </div>
  </section>

  <footer class="site-footer">
    <div class="social">
      <svg width="26" height="26" viewBox="0 0 26 26" aria-label="Social link"><circle cx="13" cy="13" r="11.5" fill="none" stroke="#f2f2f2" stroke-width="1.5"/></svg>
      <svg width="26" height="26" viewBox="0 0 26 26" aria-label="Social link"><circle cx="13" cy="13" r="11.5" fill="none" stroke="#f2f2f2" stroke-width="1.5"/></svg>
      <svg width="26" height="26" viewBox="0 0 26 26" aria-label="Social link"><circle cx="13" cy="13" r="11.5" fill="none" stroke="#f2f2f2" stroke-width="1.5"/></svg>
    </div>
    <p class="contact-line">48 Harbor Ln Kingsport, California 90511 info@lanternpubkq.com</p>
    <div class="group-mark">Halden Group</div>
  </footer>
</body>
</html>
```